New business card design needed for Diesel Fitting (Mechanical) Company

We need a new business card for our company called "Granite Valley Engineering" that showcases our logo and business details.
Target Market(s)
Owners of all makes and models of vehicles, trucks, plant and machinery.
Industry/Entity Type
Mechanical
Contact Information for Business Card
The business card details need to include the following: Owners/Directors: Trevor & Marisol Dunn-Calloway ABN: 47 913 206 781 Address: 561 Beaumont Street CHARTERS TOWERS QLD 4820 Postal Address: PO Box 8716 CHARTERS TOWERS QLD 4820 Website: www.gvengineering.com.au Phone: 4732 9185 Mobile: 0491 375 806 Emails: sales@gvengineering.com.au; admin@gvengineering.com.au; accounts@gvengineering.com.au; parts@gvengineering.com.au; office@gvengineering.com.au, reception@gvengineering.com.au
Look and feel

```html
<!DOCTYPE html>
<html lang="en">
<head>
<meta charset="utf-8">
<title>Granite Valley Engineering – Business Card</title>
<link href="https://fonts.googleapis.com/css2?family=Roboto:ital,wght@0,400;0,700;1,700&display=swap" rel="stylesheet">
<style>
  :root {
    --backdrop: #2a2a2a;
    --card: #151515;
    --orange: #f26a1b;
    --yellow: #f7b51c;
    --red: #e5262a;
    --white: #f2f2f2;
    --grey: #9a9a9a;
  }
  * { box-sizing: border-box; margin: 0; padding: 0; }
  html, body {
    width: 1200px; height: 900px; overflow: hidden;
    background: var(--backdrop);
    font-family: "Roboto", Arial, sans-serif;
  }
  .card {
    position: absolute; left: 100px; top: 164px;
    width: 1000px; height: 572px;
    background: var(--card);
    box-shadow: 0 18px 40px rgba(0,0,0,.5);
    overflow: hidden;
  }
  .brand {
    position: absolute; left: 70px; top: 110px;
    display: flex; align-items: center; gap: 18px;
  }
  .brand-dot {
    width: 54px; height: 54px; border-radius: 50%;
    background: var(--orange); flex: none;
  }
  .brand-name {
    color: var(--orange); font-weight: 700;
    font-size: 40px; line-height: 1.1;
  }
  .divider {
    position: absolute; left: 505px; top: 60px;
    width: 2px; height: 290px; background: var(--orange);
  }
  .details {
    position: absolute; left: 535px; top: 62px;
    color: var(--white); font-size: 19px; line-height: 1.32;
  }
  .owner-name {
    color: var(--orange); font-weight: 700; font-style: italic;
    font-size: 27px; line-height: 1.2;
  }
  .owner-role { color: var(--grey); font-size: 18px; margin-bottom: 8px; }
  .label { color: var(--yellow); }
  .contact-line { display: flex; align-items: center; gap: 10px; }
  .contact-line svg { width: 16px; height: 16px; flex: none; }
  .contacts { margin-top: 6px; }
  .emails {
    position: absolute; left: 70px; top: 420px;
    color: var(--white); font-size: 18px; line-height: 1.55;
  }
  .bullet { color: var(--yellow); margin: 0 6px; }
  .accent-bar {
    position: absolute; left: 0; bottom: 0;
    width: 100%; height: 7px;
    background: linear-gradient(90deg, var(--yellow), var(--orange) 55%, var(--red));
  }
</style>
</head>
<body>
  <div class="card">
    <div class="brand">
      <span class="brand-dot"></span>
      <span class="brand-name">Granite Valley<br>Engineering</span>
    </div>

    <div class="divider"></div>

    <div class="details">
      <p class="owner-name">Trevor &amp; Marisol Dunn-Calloway</p>
      <p class="owner-role">Owners/Directors</p>
      <p><span class="label">Address:</span> 561 Beaumont Street</p>
      <p>Charters Towers, QLD 4820</p>
      <p><span class="label">Postal Address:</span> PO Box 8716</p>
      <p>Charters Towers, QLD 4820</p>
      <div class="contacts">
        <p class="contact-line">
          <svg viewBox="0 0 16 16" aria-hidden="true"><path fill="#f7b51c" d="M3.5 1.5l2.5 0 1 3.5-1.6 1.2a8 8 0 0 0 4.4 4.4l1.2-1.6 3.5 1v2.5c0 .8-.7 1.5-1.5 1.5A12.5 12.5 0 0 1 2 3c0-.8.7-1.5 1.5-1.5z"/></svg>
          07 4732 9185
        </p>
        <p class="contact-line">
          <svg viewBox="0 0 16 16" aria-hidden="true"><rect x="4" y="1" width="8" height="14" rx="1.5" fill="none" stroke="#f7b51c" stroke-width="1.6"/><circle cx="8" cy="12.3" r="1" fill="#f7b51c"/></svg>
          0491 375 806
        </p>
        <p class="contact-line">
          <svg viewBox="0 0 16 16" aria-hidden="true"><circle cx="8" cy="8" r="6.5" fill="none" stroke="#f7b51c" stroke-width="1.5"/><path d="M1.5 8h13M8 1.5c-3 3.5-3 9.5 0 13M8 1.5c3 3.5 3 9.5 0 13" fill="none" stroke="#f7b51c" stroke-width="1.2"/></svg>
          www.gvengineering.com.au
        </p>
      </div>
    </div>

    <div class="emails">
      <p>sales@gvengineering.com.au<span class="bullet">•</span>admin@gvengineering.com.au<span class="bullet">•</span>accounts@gvengineering.com.au</p>
      <p>parts@gvengineering.com.au<span class="bullet">•</span>office@gvengineering.com.au<span class="bullet">•</span>reception@gvengineering.com.au</p>
    </div>

    <div class="accent-bar"></div>
  </div>
</body>
</html>
```